Ecommerce Website

Hello designers of Pixel Bazaar,

Today I'm requesting webpage designs for my new start up business in Toronto Canada. I have little or no experience in this field so I decided to outsource it here! My business revolves around the retail of customizable smartphone cases, as well as other objects such as mouse pads, mugs, etc.. Our main focus is smartphone cases, tablets and such. There are a few of these types of websites out already so the idea shouldn't be too foreign. I am looking for a minimalist look for my website revolving around light colours. Should convey a sense of simplistic design with elegant feel while including aspects of the business. Please see current website at brightcasewerk.ca to see how the set-up is (currently on pre-made template). Should have a similar feel to it. Also i have a post for logo design as i currently do not have one. If you can create a logo as well for my other post along with this one, gives preference to artist.

http://jobs.pixelbazaar.com/job.aspx?id=987612
Updates

The design should be transferable to the other webpages on the site. The overall look should be the same (borders, buttons, etc)

I am not sure if I'm allowed to request the page in coding as it said non-coded earlier. However it would be preferable to have the website in CSS or HTML as well as a PSD version for alterations.

Wasn't too clear about the total requirements. We are looking for a main homepage as well as a general design for the rest of our pages such as browsing catalogue page, product page, etc.. Should be a general look that can be used for multiple pages.

I have committed the payment so please do not hesitate to post designs.

To All designers.  I have attached the logo to the brief. It has multiple colors which you can choose from. The last one on the second row is the one i prefer the best however if your site can match well with any other ones, that is okay as well. 

Reason: have a few designs for selection in mind however need to get it to the final point.

Target Market(s)

Young adults ages 19 - 32

Industry/Entity Type

Retail

Requirements
Must have
• Main slider design - Main page will have a slider which displays new products or services. Please see brightcasewerk.ca for example

Note worthy - Currently we are using a service from http://www.printlumo.com/ so please make sure that it the design will work with that in mind.

```html
<!DOCTYPE html>
<html lang="en">
<head>
<meta charset="utf-8">
<title>BrightCaseWerk – Home</title>
<link rel="stylesheet" href="https://fonts.googleapis.com/css2?family=Open+Sans:wght@400;600;700&family=Cinzel:wght@400;600&family=Archivo+Black&display=swap">
<style>
  :root {
    --brand-blue: #2a9cc3;
    --accent-yellow: #fbb11c;
    --hero-light: #dce8ee;
    --hero-mid: #b9cfd9;
    --ink: #1b1b1b;
    --muted: #8a8a8a;
    --rule: #d6d6d6;
    --white: #ffffff;
  }
  * { box-sizing: border-box; margin: 0; padding: 0; }
  html, body { width: 882px; height: 1200px; overflow: hidden; background: var(--white); }
  body { position: relative; font-family: "Open Sans", Arial, sans-serif; color: var(--ink); }

  /* Header */
  .site-header { position: absolute; left: 0; top: 0; width: 882px; height: 75px; background: var(--brand-blue); }
  .brand { position: absolute; left: 106px; top: 28px; display: flex; align-items: center; gap: 7px; color: var(--white); font-size: 13px; font-weight: 400; }
  .brand-dot { width: 14px; height: 14px; border-radius: 50%; background: var(--white); }
  .main-nav { position: absolute; left: 288px; top: 35px; display: flex; gap: 13px; }
  .main-nav a { display: flex; align-items: center; gap: 6px; color: var(--white); text-decoration: none; font-size: 13px; }
  .main-nav svg { width: 17px; height: 17px; stroke: var(--white); fill: none; stroke-width: 1.6; }

  /* Hero slider */
  .hero { position: absolute; left: 0; top: 75px; width: 882px; height: 290px; border-bottom: 3px solid var(--brand-blue);
          background: radial-gradient(ellipse at 20% 40%, var(--hero-mid), transparent 60%), linear-gradient(120deg, var(--hero-light), #eef4f7 55%, var(--hero-mid)); }
  .tile { position: absolute; width: 123px; height: 104px; border: 1px solid var(--white); }
  .tile-promo { background: var(--accent-yellow); color: var(--white); font-family: "Archivo Black", Arial, sans-serif; line-height: 1.05; }
  .tile-photo.laptop { background: linear-gradient(180deg, #b9cbd2, #d7d4cb 60%, #e8e2d4); }
  .tile-photo.shirt { background: linear-gradient(160deg, #2c2c2c, #3f6f9a 55%, #2a2a2a); }
  .tile-photo.hand { background: linear-gradient(150deg, #f2f2f2, #d7b9a6 60%, #e6e6e6); }
  .promo-lap { left: 234px; top: 32px; padding: 26px 0 0 22px; }
  .promo-lap .big { font-size: 17px; }
  .promo-lap .small { font-size: 10px; }
  .promo-shirt { left: 358px; top: 136px; padding: 14px 0 0 12px; }
  .promo-shirt .big { font-size: 16px; }
  .promo-shirt .mid { font-size: 12px; }
  .promo-shirt .fine { font-family: "Open Sans", Arial, sans-serif; font-size: 8px; margin-top: 6px; padding-left: 2px; }
  .promo-phone { left: 605px; top: 136px; padding: 28px 0 0 0; text-align: center; }
  .promo-phone .fine { font-size: 9px; }
  .promo-phone .big { font-size: 16px; margin-top: 3px; }
  .promo-phone .mid { font-size: 12px; margin-top: 3px; }

  /* Sections */
  .section-title { position: absolute; left: 0; width: 882px; text-align: center; font-weight: 700; font-size: 22px; letter-spacing: 0.3px; }
  .section-sub { position: absolute; left: 0; width: 882px; text-align: center; font-family: "Cinzel", Georgia, serif; font-size: 12px; color: var(--muted); letter-spacing: 0.5px; }
  .rule { position: absolute; left: 264px; width: 366px; height: 1px; background: var(--rule); }

  .feature { position: absolute; width: 160px; text-align: center; top: 499px; }
  .feature-icon { width: 108px; height: 108px; border-radius: 50%; background: var(--accent-yellow); margin: 0 auto; display: flex; align-items: center; justify-content: center; }
  .feature-icon svg { width: 56px; height: 56px; fill: var(--white); }
  .feature-title { margin-top: 21px; font-family: "Cinzel", Georgia, serif; font-size: 13px; letter-spacing: 0.5px; }
  .feature-sub { font-family: "Cinzel", Georgia, serif; font-size: 8.5px; color: var(--muted); letter-spacing: 0.5px; }

  .category-picker { position: absolute; left: 653px; top: 530px; width: 143px; }
  .picker-label { font-family: "Cinzel", Georgia, serif; font-size: 12px; }
  .picker-sub { font-family: "Cinzel", Georgia, serif; font-size: 8.5px; color: #555; letter-spacing: 0.4px; }
  .picker-hint { margin-top: 8px; font-size: 10px; color: var(--accent-yellow); }
  .picker-select { margin-top: 6px; height: 30px; border: 1px solid #c8c8c8; display: flex; align-items: center; justify-content: center; font-size: 10.5px; color: #444; position: relative; }
  .picker-select svg { position: absolute; right: 12px; top: 10px; width: 11px; height: 8px; stroke: #444; fill: none; stroke-width: 1.6; }

  .product { position: absolute; text-align: center; font-family: "Cinzel", Georgia, serif; font-size: 11px; line-height: 13px; color: var(--ink); }
  .product-shot { position: absolute; border-radius: 10px; }
  .shot-aurora { left: 171px; top: 830px; width: 156px; height: 105px; background: linear-gradient(150deg, #e8eaec, #9ea6ad 60%, #f2f3f4); transform: skewX(-10deg); border-radius: 20px; }
  .shot-mini { left: 425px; top: 825px; width: 50px; height: 124px; background: linear-gradient(180deg, #d9dcdf, #5f88b3 45%, #d9dcdf); }
  .shot-slide { left: 602px; top: 866px; width: 112px; height: 78px; background: linear-gradient(180deg, #e6e8ea, #9fb0c0 50%, #cfd3d6); border-radius: 8px; }

  /* Footer */
  .footer-rule { position: absolute; left: 246px; top: 1056px; width: 368px; height: 1px; background: var(--rule); }
  .footer-col { position: absolute; top: 1077px; font-size: 7px; color: #555; }
  .footer-col h4 { font-family: "Cinzel", Georgia, serif; font-size: 9.5px; font-weight: 600; color: var(--ink); margin-bottom: 9px; }
  .footer-col ul { list-style: none; }
  .footer-col li { margin-bottom: 7px; }
  .footer-copy { width: 145px; line-height: 9.5px; }
  .branch { display: flex; gap: 9px; align-items: flex-start; margin-bottom: 6px; line-height: 9px; width: 130px; }
  .branch svg { width: 11px; height: 11px; fill: var(--ink); flex: none; }
  .footer-bar { position: absolute; left: 200px; top: 1166px; width: 482px; height: 34px; background: var(--brand-blue); color: var(--white); font-size: 7.5px; display: flex; align-items: center; justify-content: center; letter-spacing: 0.3px; }
</style>
</head>
<body>

<header class="site-header">
  <div class="brand"><span class="brand-dot"></span>BrightCaseWerk</div>
  <nav class="main-nav">
    <a href="#"><svg viewBox="0 0 18 18"><path d="M2 9 9 3l7 6M4 8v7h4v-4h2v4h4V8" fill="#fff"/></svg>Home</a>
    <a href="#"><svg viewBox="0 0 18 18"><path d="M3 3l12 13"/></svg>Designs</a>
    <a href="#"><svg viewBox="0 0 18 18"><path d="M9 2a5 5 0 0 0-3 9v3h6v-3a5 5 0 0 0-3-9zM7 16h4"/></svg>Create</a>
    <a href="#"><svg viewBox="0 0 18 18"><ellipse cx="9" cy="8" rx="7.5" ry="5"/><path d="M5 12l-2 4 5-3"/></svg>About</a>
    <a href="#"><svg viewBox="0 0 18 18"><path d="M1 9 17 2l-4 14-4-5-8-2zM9 11l8-9"/></svg>Contact</a>
    <a href="#"><svg viewBox="0 0 18 18"><path d="M2 9 9 2h7v7l-7 7z"/><circle cx="13" cy="5" r="1.2"/></svg>Request a Quote</a>
  </nav>
</header>

<section class="hero" aria-label="Featured products slider">
  <div class="tile tile-promo promo-lap"><div class="big">CHANGE</div><div class="small">YOUR LAP<br>LAYOUT :)</div></div>
  <div class="tile tile-photo laptop" style="left:358px;top:32px" role="img" aria-label="Photo of a laptop on a beach"></div>
  <div class="tile tile-photo hand" style="left:605px;top:34px" role="img" aria-label="Photo of hands holding a smartphone"></div>
  <div class="tile tile-promo promo-shirt"><div class="big">DESIGN</div><div class="mid">T-SHIRT ?</div><div class="fine">PUT EVEN YOUR DOG?</div></div>
  <div class="tile tile-photo shirt" style="left:482px;top:136px" role="img" aria-label="Photo of a blue printed t-shirt"></div>
  <div class="tile tile-promo promo-phone"><div class="fine">DESIGN YOUR</div><div class="big">SMART</div><div class="mid">PHONE ?</div></div>
</section>

<h2 class="section-title" style="top:405px">DESIGN ALL THINGS</h2>
<p class="section-sub" style="top:437px">Use your imaganation as can you do, you will get</p>
<div class="rule" style="top:475px"></div>

<div class="feature" style="left:93px">
  <div class="feature-icon"><svg viewBox="0 0 56 56"><path d="M28 6a15 15 0 0 0-9 27c2 2 3 4 3 7h12c0-3 1-5 3-7A15 15 0 0 0 28 6z"/><rect x="22" y="42" width="12" height="3" rx="1"/><rect x="23" y="46.5" width="10" height="3" rx="1"/></svg></div>
  <div class="feature-title">HAVE AN IDEA</div>
  <div class="feature-sub">SIMPLY MAKE IT</div>
</div>
<div class="feature" style="left:273px">
  <div class="feature-icon"><svg viewBox="0 0 56 56"><path d="M8 16h12a5 5 0 1 1 8 0h12v11a5 5 0 1 0 0 8v11H28a5 5 0 1 0-8 0H8V35a5 5 0 1 1 0-8z"/></svg></div>
  <div class="feature-title">DESIGN IT</div>
  <div class="feature-sub">BY YOUR SELF</div>
</div>
<div class="feature" style="left:452px">
  <div class="feature-icon" role="img" aria-label="Signature flourish emblem"></div>
  <div class="feature-title">MAKE YOUR</div>
  <div class="feature-sub">OWN SIGNATURE</div>
</div>

<div class="category-picker">
  <div class="picker-label">FROM</div>
  <div class="picker-sub">UNLIMATED CATAGORY</div>
  <div class="picker-hint">Select your&nbsp; favorite section</div>
  <div class="picker-select">Mobile<svg viewBox="0 0 11 8"><path d="M1 1l4.5 5L10 1"/></svg></div>
</div>

<div class="rule" style="top:695px"></div>
<h2 class="section-title" style="top:710px">GET STARTED NOW</h2>
<p class="section-sub" style="top:742px">Use your imaganation as can you do, you will get</p>
<div class="rule" style="top:785px"></div>

<div class="product-shot shot-aurora" role="img" aria-label="Photo of the Aurora One S phone"></div>
<div class="product-shot shot-mini" role="img" aria-label="Photo of the Kestrel Mini phone"></div>
<div class="product-shot shot-slide" role="img" aria-label="Photo of the Kestrel Slide phone"></div>

<div class="product" style="left:141px;top:962px;width:160px">Aurora One S<br>Decorate from $25 CAD</div>
<div class="product" style="left:364px;top:962px;width:160px">Kestrel Mini<br>Decorate from $0 CAD</div>
<div class="product" style="left:565px;top:962px;width:160px">Kestrel Slide<br>Decorate from $0 CAD</div>

<div class="footer-rule"></div>
<div class="footer-col" style="left:240px">
  <h4>HOME</h4>
  <ul><li>ABOUT</li><li>SERVICES</li><li>CONTACT US</li></ul>
</div>
<div class="footer-col" style="left:352px">
  <h4>MENU</h4>
  <p class="footer-copy">benign&nbsp; any useful data, but serves to reserve space enign&nbsp; any useful data, but serves to reserve space where real data is nominally……</p>
</div>
<div class="footer-col" style="left:532px">
  <h4>BRANCH</h4>
  <div class="branch"><svg viewBox="0 0 11 11"><path d="M5.5 0a4 4 0 0 0-4 4c0 3 4 7 4 7s4-4 4-7a4 4 0 0 0-4-4z"/></svg><span>48 LINDEL WAY, TORVIK</span></div>
  <div class="branch"><svg viewBox="0 0 11 11"><path d="M5.5 0a4 4 0 0 0-4 4c0 3 4 7 4 7s4-4 4-7a4 4 0 0 0-4-4z"/></svg><span>BRANCH2: Corvale 145 Ostmere<br>Lane, Suite 2.</span></div>
</div>

<footer class="footer-bar">ALLRIGHTS RESEVED BY BRIGHTCASEWERK @2013</footer>

</body>
</html>
```